Business Card Design for Venture Kite

Venture Kite is a pro bono student consultancy service offered by Corvala KTRB to social start ups and enterprises. We provide consulting services with expertise in areas such as Marketing, IT, Business Strategy and Innovation.
I have attached\ the Venture Kite Logo here for your perusal.
Industry/Entity Type
Business
Contact Information for Business Card
Name: Ha Min Park Name: Thomas Leung
Role: Project Leader Role: Vice Project Leader
M:0477203941 M: 0479352806
E: ha-min.park@corvalaktrb.org E: thomas.leung@corvalaktrb.org
W: www.corvalaktrb.org W: www.corvalaktrb.org

```html
<!DOCTYPE html>
<html lang="en">
<head>
<meta charset="utf-8">
<title>Venture Kite — Business Card</title>
<link rel="stylesheet" href="https://fonts.googleapis.com/css2?family=Oswald:wght@600&family=Open+Sans:wght@600&display=swap">
<style>
  :root {
    --brand-orange: #f3921f;
    --card-white: #ffffff;
    --ink: #151515;
    --backdrop: #d9d9d9;
    --text-light: #ffffff;
  }
  * { margin: 0; padding: 0; box-sizing: border-box; }
  html, body {
    width: 1200px;
    height: 900px;
    overflow: hidden;
    background: var(--backdrop);
  }
  .canvas {
    position: relative;
    width: 1200px;
    height: 900px;
    display: flex;
    flex-direction: column;
    align-items: center;
    justify-content: center;
    gap: 40px;
  }
  .card {
    position: relative;
    width: 630px;
    height: 360px;
    overflow: hidden;
    box-shadow: 0 6px 18px rgba(0, 0, 0, 0.18);
  }
  .card-back { background: var(--brand-orange); }
  .card-front { background: var(--card-white); }
  .card-shape {
    position: absolute;
    inset: 0;
    width: 100%;
    height: 100%;
  }
  .wordmark {
    position: absolute;
    font-family: "Oswald", sans-serif;
    font-weight: 600;
    color: var(--ink);
    text-transform: uppercase;
    text-align: center;
    line-height: 1.02;
    letter-spacing: 0.5px;
  }
  .card-back .wordmark {
    left: 0;
    right: 0;
    top: 50%;
    transform: translateY(-50%);
    font-size: 44px;
  }
  .card-front .wordmark {
    left: 30px;
    width: 210px;
    top: 50%;
    transform: translateY(-50%);
    font-size: 42px;
  }
  .contact-list {
    position: absolute;
    left: 380px;
    top: 110px;
    list-style: none;
    font-family: "Open Sans", sans-serif;
    font-weight: 600;
    font-size: 14px;
    color: var(--text-light);
  }
  .contact-item {
    display: flex;
    align-items: center;
    gap: 12px;
    height: 20px;
    margin-bottom: 26px;
  }
  .contact-icon {
    width: 14px;
    height: 14px;
    flex: none;
  }
</style>
</head>
<body>
<main class="canvas">
  <section class="card card-back" aria-label="Card back">
    <p class="wordmark">Venture<br>Kite</p>
  </section>

  <section class="card card-front" aria-label="Card front">
    <svg class="card-shape" viewBox="0 0 630 360" preserveAspectRatio="none" aria-hidden="true">
      <path d="M 300 0 Q 200 170 232 360 L 630 360 L 630 0 Z" fill="var(--brand-orange)"/>
    </svg>
    <p class="wordmark">Venture<br>Kite</p>
    <ul class="contact-list">
      <li class="contact-item">
        <svg class="contact-icon" viewBox="0 0 14 14" aria-hidden="true">
          <rect x="3.5" y="0.8" width="7" height="12.4" rx="1.3" fill="none" stroke="#fff" stroke-width="1.4"/>
          <circle cx="7" cy="10.8" r="0.8" fill="#fff"/>
        </svg>
        <span>0477203941</span>
      </li>
      <li class="contact-item">
        <svg class="contact-icon" viewBox="0 0 14 14" aria-hidden="true">
          <rect x="0.5" y="2.5" width="13" height="9" fill="#fff"/>
          <path d="M0.8 2.8 L7 8 L13.2 2.8" fill="none" stroke="var(--brand-orange)" stroke-width="1.2"/>
        </svg>
        <span>ha-min.park@corvalaktrb.org</span>
      </li>
      <li class="contact-item">
        <svg class="contact-icon" viewBox="0 0 14 14" aria-hidden="true">
          <g fill="none" stroke="#fff" stroke-width="1.2">
            <circle cx="7" cy="7" r="6"/>
            <ellipse cx="7" cy="7" rx="2.6" ry="6"/>
            <path d="M1 7 H13 M2 3.8 H12 M2 10.2 H12"/>
          </g>
        </svg>
        <span>www.corvalaktrb.org</span>
      </li>
    </ul>
  </section>
</main>
</body>
</html>
```